依頼詳細
オープン前のプレオープンで使用するチラシ依頼です。
キャンペーン価格で5日間限定で初回は初見料と施術代で9000円が500円1日限定で10名

こんなお困りの症状はありませんか?

・整体やマッサージに通っているが、肩がこって仕事や日常生活がつらい
・腰痛で電気をあてたり、整骨院に行っても変化がなく諦めている
・頻繁に頭痛に襲われて辛いので、その度に頭痛薬を飲む
・生理前後に痛みが強く、鎮痛薬を飲んでしまう
・精神薬を処方されたが、いつまで飲み続けるのか不安だけどやめられない
・病院で薬をもらったが一向にめまいが改善しない
の項目はなるべく全部入れたいです。

女性に特化した整体院なのでそこがイメージしやすいデザインがありがたいです。
記載項目
店名:自律神経専門 整体院 ゆらぎ→自律神経専門を目立たせて欲しいです。

URL:https://yuragi-karada.example/

地図→詳細を送りますので作成して頂きたいです。

スタッフ写真もしくは女性が施術している写真を入れて欲しいです。

マンションの外装写真を入れるか目印のマルカワ堂がすぐ近く(ビル1つとなり)なので場所イメージがついたほうがいい気がするのでそこの情報はどちらか入れたいです。
電話番号とラインに関しては7月中に取得します。

院内
・予約優先制
・女性セラピスト指名OK
・施術ルーム完全個室
・キッズスペースあり
・ロゴ
を入れたいです。

サイズ
A4
ページ数
両面
希望イメージ
シンプル 複雑
単色 カラフル
暗い 明るい
日常 高級
遊び心 厳粛
未来的 伝統的
女性的 男性的
希望する色
赤系、緑系、茶系
納品ファイル
• 高解像度JPG (.jpg)
• PNG形式 (.png)
補足説明
可能であれば当社でも内容を修正することができれば助かります。
出来る限りインパクトの強いチラシが希望です。

「自律神経専門」整体院の自律神経専門が目立ちたいです。
宜しくお願い致します。

```html
<!DOCTYPE html>
<html lang="ja">
<head>
<meta charset="UTF-8">
<title>自律神経専門 整体院 ゆらぎ オープンキャンペーン</title>
<link href="https://fonts.googleapis.com/css2?family=Noto+Serif+JP:wght@500;700;900&family=Noto+Sans+JP:wght@400;500;700&family=Great+Vibes&display=swap" rel="stylesheet">
<style>
:root{
  --green:#3f9a3b;
  --green-dark:#2d7a2c;
  --pink:#e88ea4;
  --pink-pale:#fbe6ea;
  --red:#d64545;
  --text:#333;
  --cream:#fdfbf6;
}
*{margin:0;padding:0;box-sizing:border-box}
html,body{width:846px;height:1200px;overflow:hidden}
body{font-family:"Noto Sans JP",sans-serif;color:var(--text);background:var(--cream)}
.flyer{position:relative;width:846px;height:1200px;overflow:hidden;background:var(--cream)}

.hero-photo{position:absolute;left:0;top:0;width:846px;height:657px;
  background:
    radial-gradient(ellipse 200px 240px at 640px 230px,#e9cbbf 0%,rgba(233,203,191,0) 100%),
    radial-gradient(ellipse 260px 160px at 520px 120px,#f7f7f5 0%,rgba(247,247,245,0) 100%),
    radial-gradient(ellipse 300px 220px at 700px 560px,#ffffff 0%,rgba(255,255,255,0) 100%),
    linear-gradient(115deg,#f2ece8 0%,#efe0da 40%,#e6cfc7 65%,#f6efec 100%)}

.brand-panel{position:absolute;left:80px;top:0;width:204px;height:600px;background:rgba(255,255,255,.92);
  display:flex;flex-direction:row-reverse;justify-content:center;gap:8px;padding:36px 8px 0}
.brand-panel p,.brand-panel h1{writing-mode:vertical-rl;line-height:1}
.tagline{font-family:"Noto Serif JP",serif;font-weight:700;font-size:36px;color:var(--green-dark);letter-spacing:.02em}
.specialty{background:var(--green);color:#fff;font-family:"Noto Serif JP",serif;font-weight:900;
  font-size:62px;padding:40px 8px;height:520px;text-align:center;margin-top:-36px}
.clinic-name{display:flex;flex-direction:column;align-items:center;gap:10px;padding-top:200px}
.clinic-name .mark{width:38px;height:38px;border-radius:50%;background:var(--green)}
.clinic-name .name{writing-mode:vertical-rl;font-family:"Noto Serif JP",serif;font-weight:900;font-size:40px;color:var(--green-dark);line-height:1}

.new-open{position:absolute;left:400px;top:400px;font-family:"Great Vibes",cursive;font-size:96px;color:var(--pink);transform:rotate(-6deg);line-height:1;white-space:nowrap}

.campaign{position:absolute;left:655px;top:490px;width:176px;height:176px;border-radius:50%;background:#fff;border:3px solid var(--pink-pale);
  display:flex;flex-direction:column;align-items:center;justify-content:center;text-align:center}
.campaign .title{font-family:"Noto Serif JP",serif;font-weight:700;color:var(--red);font-size:19px;line-height:1.25}
.campaign .price{display:flex;align-items:center;gap:4px;margin-top:6px}
.campaign .before{font-size:11px;color:#666;line-height:1.2}
.campaign .before s{font-size:13px}
.campaign .arrow{color:var(--red);font-size:14px}
.campaign .after{font-family:"Noto Serif JP",serif;font-weight:900;color:var(--red);font-size:36px;line-height:1}
.campaign .after small{font-size:16px}
.limit{position:absolute;left:590px;top:660px;width:240px;background:var(--red);color:#fff;font-weight:700;font-size:15px;text-align:center;padding:6px 0;white-space:nowrap}

.lead{position:absolute;left:60px;top:684px;width:490px;border:2px solid var(--green);border-radius:10px;background:#fff;
  padding:14px 10px;font-family:"Noto Serif JP",serif;font-weight:700;font-size:21px;color:var(--green-dark);line-height:1.6;text-align:center}

.symptoms{position:absolute;left:60px;top:806px;width:500px}
.symptoms h2{font-family:"Noto Serif JP",serif;font-size:19px;color:var(--green-dark);margin-bottom:8px;border-bottom:2px dotted var(--green);padding-bottom:5px}
.symptoms li{list-style:none;display:flex;gap:7px;font-size:12.5px;line-height:1.4;margin-bottom:6px;white-space:nowrap}
.symptoms li svg{flex:none;margin-top:1px}

.illustrations{position:absolute;left:60px;top:1020px;width:490px;display:flex;justify-content:space-between}
.illustrations figure{width:112px;text-align:center}
.illustrations .art{width:112px;height:90px;border-radius:50% 50% 8px 8px;
  background:radial-gradient(circle at 50% 40%,#f3dccf 0%,#e7c9bb 45%,#f7eee9 100%)}
.illustrations figure:nth-child(2) .art{background:radial-gradient(circle at 50% 40%,#f1d6c6 0%,#d9b8a6 45%,#f5ece6 100%)}
.illustrations figure:nth-child(3) .art{background:radial-gradient(circle at 50% 40%,#f4e1d2 0%,#e2cdb0 45%,#f6f0e6 100%)}
.illustrations figure:nth-child(4) .art{background:radial-gradient(circle at 50% 40%,#f2d9d0 0%,#dcc3c4 45%,#f6eeee 100%)}
.illustrations figcaption{margin-top:4px;font-size:11px;background:#fff;border:1px solid #ccc;padding:2px 0;white-space:nowrap}

.closing{position:absolute;left:60px;top:1140px;width:490px;background:var(--green);color:#fff;font-weight:700;font-size:16px;text-align:center;padding:9px 0;border-radius:4px;white-space:nowrap}

.points{position:absolute;left:580px;top:708px;width:250px;height:380px;display:flex;flex-direction:row-reverse;justify-content:center;gap:12px}
.points p{writing-mode:vertical-rl;font-family:"Noto Serif JP",serif;font-weight:900;line-height:1;white-space:nowrap}
.points .p1{font-size:36px;color:var(--green-dark)}
.points .p2{font-size:36px;color:var(--green)}
.points .p3{font-size:34px;color:var(--green-dark);padding-top:20px}
</style>
</head>
<body>
<main class="flyer">
  <div class="hero-photo" role="img" aria-label="白衣の女性セラピストが女性の肩を施術している写真"></div>

  <section class="brand-panel">
    <p class="tagline">女性のための整体院</p>
    <h1 class="specialty">自律神経専門</h1>
    <div class="clinic-name"><span class="mark"></span><span class="name">ゆらぎ整体院</span></div>
  </section>

  <p class="new-open">New Open</p>

  <section class="campaign">
    <p class="title">オープン<br>キャンペーン</p>
    <div class="price">
      <p class="before">初回料<br><s>9,000円</s></p>
      <span class="arrow">▶</span>
      <p class="after">500<small>円</small></p>
    </div>
  </section>
  <p class="limit">1日10名様・5日間限定</p>

  <p class="lead">病院や他の整骨院に行っても、<br>薬を飲んでも良くならなかった…</p>

  <section class="symptoms">
    <h2>こんなお困りの症状はありませんか？</h2>
    <ul>
      <li><svg width="15" height="15" viewBox="0 0 16 16"><rect x="1" y="1" width="14" height="14" fill="none" stroke="#3f9a3b" stroke-width="1.6"/><path d="M4 8l3 3 6-7" fill="none" stroke="#d64545" stroke-width="2"/></svg>整体やマッサージに通っているが、肩がこって仕事や日常生活がつらい</li>
      <li><svg width="15" height="15" viewBox="0 0 16 16"><rect x="1" y="1" width="14" height="14" fill="none" stroke="#3f9a3b" stroke-width="1.6"/><path d="M4 8l3 3 6-7" fill="none" stroke="#d64545" stroke-width="2"/></svg>腰痛で電気をあてたり、整骨院に行っても変化がなく諦めている</li>
      <li><svg width="15" height="15" viewBox="0 0 16 16"><rect x="1" y="1" width="14" height="14" fill="none" stroke="#3f9a3b" stroke-width="1.6"/><path d="M4 8l3 3 6-7" fill="none" stroke="#d64545" stroke-width="2"/></svg>頻繁に頭痛に襲われて辛いので、その度に頭痛薬を飲む</li>
      <li><svg width="15" height="15" viewBox="0 0 16 16"><rect x="1" y="1" width="14" height="14" fill="none" stroke="#3f9a3b" stroke-width="1.6"/><path d="M4 8l3 3 6-7" fill="none" stroke="#d64545" stroke-width="2"/></svg>生理前後に痛みが強く、鎮痛薬を飲んでしまう</li>
      <li><svg width="15" height="15" viewBox="0 0 16 16"><rect x="1" y="1" width="14" height="14" fill="none" stroke="#3f9a3b" stroke-width="1.6"/><path d="M4 8l3 3 6-7" fill="none" stroke="#d64545" stroke-width="2"/></svg>精神薬を処方されたが、いつまで飲み続けるのか不安だけどやめられない</li>
      <li><svg width="15" height="15" viewBox="0 0 16 16"><rect x="1" y="1" width="14" height="14" fill="none" stroke="#3f9a3b" stroke-width="1.6"/><path d="M4 8l3 3 6-7" fill="none" stroke="#d64545" stroke-width="2"/></svg>病院で薬をもらったが一向にめまいが改善しない</li>
    </ul>
  </section>

  <section class="illustrations">
    <figure><div class="art" role="img" aria-label="頭痛やめまいに悩む女性のイラスト"></div><figcaption>頭痛・めまい</figcaption></figure>
    <figure><div class="art" role="img" aria-label="肩や腰の痛みに悩む女性のイラスト"></div><figcaption>肩や腰の痛み</figcaption></figure>
    <figure><div class="art" role="img" aria-label="生理痛に悩む女性のイラスト"></div><figcaption>生理前後の痛み</figcaption></figure>
    <figure><div class="art" role="img" aria-label="不眠に悩む女性のイラスト"></div><figcaption>眠りが浅い</figcaption></figure>
  </section>

  <p class="closing">その身体の不調、自律神経の調整で改善させましょう</p>

  <section class="points">
    <p class="p1">改善のポイントは、</p>
    <p class="p2">自律神経の乱れの調整</p>
    <p class="p3">痛み知らずの体質へ導く</p>
  </section>
</main>
</body>
</html>
```